Lumen Peak Website - Enabling Omni channel

Slogan : Enabling Omnichannel Sales

1. Sell products via multiple sale channels
2. Access our technology and services to get your products moving through new channels
3. Customise our mobile and web technology platforms to suit your supply chain.

Slogan: Lumen peak – Innovating new business.

Use the content from these websites to create a new one
http://quorvanthq.com/
http://bralowe-designs.com/lumenPeak02/

Target Market(s)

Business and Coporations who need mobile and web technology or services to increase product sales within their vertical industry. Our case studies show the industries we have worked in; namely: Retail, wholesale, online retail, motor and auto trade. Also have rich experience in Importing and Exporting.

Industry/Entity Type

Retail

Number of Pages Required

3 page

Font styles to use
Sans Serif

Colors
0255a3
ec1f27
9bcb3c
ffffff
0792cd
ffc214

Requirements
Must have
• Punchy headline home page with possible animations or unique and interesting images

```html
<!DOCTYPE html>
<html lang="en">
<head>
<meta charset="utf-8">
<title>Lumen Peak – Enabling Omnichannel Sales</title>
<link href="https://fonts.googleapis.com/css2?family=Open+Sans:wght@300;400;600;700&display=swap" rel="stylesheet">
<style>
:root{
  --brand-blue:#0255a3;
  --nav-blue:#0a57a8;
  --sky:#0792cd;
  --sky-band:#0a6fb6;
  --navy:#0b2f78;
  --deep:#0a58a6;
  --red:#ec1f27;
  --green:#9bcb3c;
  --yellow:#ffc214;
  --white:#ffffff;
  --ink:#222a36;
  --footer:#0c4a9e;
  --footer-bar:#0a3f8a;
}
*{box-sizing:border-box;margin:0;padding:0}
html,body{width:963px;height:1200px;overflow:hidden;background:var(--white)}
body{position:relative;font-family:"Open Sans",sans-serif;color:var(--ink)}
.abs{position:absolute}

/* header */
.brand{left:96px;top:14px;}
.brand-name{font-size:24px;font-weight:700;color:var(--brand-blue);line-height:1;display:flex;align-items:center;gap:7px}
.brand-name .dot{width:12px;height:12px;background:var(--brand-blue)}
.brand-tag{font-size:12px;font-style:italic;color:var(--brand-blue);margin:6px 0 0 66px;font-weight:400}
.contact-top{right:98px;top:13px;text-align:right;font-size:13px;color:var(--ink);line-height:22px;font-weight:600}
.contact-top div{display:flex;align-items:center;justify-content:flex-end;gap:9px}

.nav{left:0;top:64px;width:963px;height:22px;background:var(--nav-blue);}
.nav ul{list-style:none;display:flex;position:absolute;right:96px;top:2px;gap:0}
.nav li{color:var(--white);font-size:13px;margin-left:41px;line-height:18px}

/* hero */
.hero{left:0;top:86px;width:963px;height:228px;background:linear-gradient(100deg,#0d2a55 0%,#1a6fb4 45%,#2b9fdc 70%,#0f3f85 100%);}
.hero-box{left:96px;top:102px;width:290px;height:197px;background:rgba(9,80,150,.78);padding:10px 14px}
.hero-box h1{font-size:24px;font-weight:700;letter-spacing:3.4px;line-height:29px;color:var(--white);margin-left:5px}
.hero-box p{font-size:13px;line-height:15.5px;color:var(--white);margin-top:3px;width:252px}
.btn{display:inline-block;background:var(--white);border-radius:4px;font-weight:600}
.hero-btn{left:179px;top:250px;width:125px;height:31px;color:var(--brand-blue);font-size:16px;line-height:31px;text-align:center}

/* channels */
.sec-title{width:963px;text-align:center;font-size:13px;font-weight:600;color:var(--ink);line-height:16px}
.card{top:358px;width:241px;height:294px;background:var(--sky);color:var(--white)}
.card .num{position:absolute;left:105px;top:5px;width:30px;height:30px;border:1.5px solid var(--white);border-radius:50%;text-align:center;font-size:17px;line-height:26px;font-weight:300}
.card .band{position:absolute;left:0;top:38px;width:100%;height:36px;background:var(--sky-band);font-size:11px;line-height:13px;display:flex;align-items:center;padding:0 22px}
.card .body{position:absolute;left:27px;top:78px;right:20px;font-size:11.5px;line-height:20px;letter-spacing:.3px}
.card .body.narrow{left:28px;right:40px}
.card.dark{background:var(--deep)}
.card.dark .band{background:var(--navy);padding-left:34px}
.card.dark .body{left:27px;line-height:16.8px}
.card .cta{position:absolute;height:19px;width:82px;color:var(--ink);font-size:11.5px;line-height:19px;text-align:center;border-radius:2px;font-weight:400;letter-spacing:.4px}
.features{list-style:none}
.features li::before{content:"▶";font-size:8px;margin-right:10px;vertical-align:1px}

/* access */
.access{left:0;top:663px;width:963px;height:301px;background:linear-gradient(180deg,#3aa4dc,#1b8fd0)}
.access-title{top:669px;color:var(--white)}
.panel{top:715px;width:340px;height:235px;color:var(--white)}
.panel.green{left:96px;background:linear-gradient(180deg,#a9d854,#8cc43a)}
.panel.yellow{left:525px;background:linear-gradient(180deg,#ffc727,#ffbe13)}
.halo{top:675px;width:93px;height:93px;border-radius:50%;background:rgba(255,255,255,.3);display:flex;align-items:center;justify-content:center}
.panel h3{position:absolute;left:23px;top:62px;right:20px;font-size:11px;font-weight:700;line-height:13.5px}
.panel p{position:absolute;left:25px;top:85px;right:30px;font-size:9.6px;line-height:19.3px;font-weight:300}
.panel ul{position:absolute;left:25px;top:81px;right:18px;list-style:none;font-size:9.6px;line-height:19.3px;font-weight:300}
.panel li{padding-left:17px;position:relative}
.panel li::before{content:"›";position:absolute;left:0;top:-3px;font-size:17px;font-weight:700}
.panel .cta{position:absolute;left:106px;top:190px;width:129px;height:32px;text-align:center;line-height:32px;font-size:13.5px;border-radius:3px}
.green .cta{color:var(--green)}
.yellow .cta{color:#f5b400}

/* customise */
.custom-title{top:979px}
.feature{display:flex;align-items:center;gap:9px;font-size:11px;color:var(--ink);font-weight:300}
.feature.wide{letter-spacing:2.4px}

/* footer */
.footer{left:0;top:1084px;width:963px;height:116px;background:var(--footer);color:var(--white)}
.footer-mark{left:96px;top:1113px;font-size:24px;font-weight:700;color:rgba(255,255,255,.14)}
.fcol{top:1098px;font-size:10px;line-height:14.5px;color:var(--white)}
.fcol h4{font-size:11px;font-weight:600;margin-bottom:5px;letter-spacing:.2px;color:var(--white)}
.fbar{left:0;top:1180px;width:963px;height:20px;background:var(--footer-bar);color:var(--white);font-size:7.5px;font-weight:700;line-height:20px}
</style>
</head>
<body>

<header>
  <div class="abs brand">
    <div class="brand-name"><span class="dot"></span>Lumen Peak</div>
    <div class="brand-tag">Enabling Omnichannel Sales</div>
  </div>
  <div class="abs contact-top">
    <div>
      <svg width="14" height="14" viewBox="0 0 24 24"><path fill="#0255a3" d="M6.6 10.8a15 15 0 0 0 6.6 6.6l2.2-2.2a1 1 0 0 1 1-.25 11 11 0 0 0 3.6.6 1 1 0 0 1 1 1V20a1 1 0 0 1-1 1A17 17 0 0 1 3 4a1 1 0 0 1 1-1h3.5a1 1 0 0 1 1 1c0 1.25.2 2.45.6 3.6a1 1 0 0 1-.25 1z"/></svg>
      <span style="margin-left:14px">+61 2 9040 7712</span>
    </div>
    <div>
      <svg width="15" height="11" viewBox="0 0 15 11"><rect x=".5" y=".5" width="14" height="10" fill="none" stroke="#0255a3"/><path d="M.5.5l7 5.5 7-5.5" fill="none" stroke="#0255a3"/></svg>
      <span>info@lumenpeak.com.au</span>
    </div>
  </div>
  <nav class="abs nav">
    <ul>
      <li>Home</li><li>About Us</li><li>Our Products</li><li>Case Studies</li><li>FAQs</li><li>Contact</li>
    </ul>
  </nav>
</header>

<section>
  <div class="abs hero" role="img" aria-label="Photo of a hand holding a glowing network of connected device icons: mail, globe, tablet, laptop, monitor, cart and media player"></div>
  <div class="abs hero-box">
    <h1>Your Partner In<br>Online Retailing</h1>
    <p>We can position your products, services and brand in front of millions of new online customers in your Retail, Wholesale, Online Retail, Motor and Auto trade</p>
  </div>
  <span class="abs btn hero-btn">Get Started</span>
</section>

<section>
  <h2 class="abs sec-title" style="top:328px">SELL PRODUCTS VIA MULTIPLE SALE CHANNELS</h2>

  <article class="abs card" style="left:96px">
    <div class="num">1</div>
    <div class="band">TECHNOLOGY AT YOUR FINGERTIPS</div>
    <p class="body narrow">We’ve developed a range of solutions that can start revolutionising your business’ supply chain process now. Or, we can help you make your custom software application, a reality.</p>
    <span class="btn cta" style="left:72px;top:221px">Start Now</span>
  </article>

  <article class="abs card dark" style="left:361px">
    <div class="num">2</div>
    <div class="band">VELTRIX – READY TO WORK<br>END-TO-END AUTOMATION</div>
    <p class="body">Increasing sales, streamlining processes, minimising errors and reducing costs are all possibilities when you automate your business using our Veltrix platform. You’ll be able to manage multi-channel selling on Bidmart, webstores, apps and traditional store inventory, build your supply chain including global drop-shipping and more.</p>
    <span class="btn cta" style="left:80px;top:268px">Start Now</span>
  </article>

  <article class="abs card" style="left:626px">
    <div class="num">3</div>
    <div class="band" style="justify-content:center">FEATURES AND MODULES</div>
    <ul class="body features" style="left:14px">
      <li>Product cataloguing</li>
      <li>Product listing</li>
      <li>Quoting</li>
      <li>Sales team catalogue &amp; quoting</li>
      <li>Managtement</li>
      <li>E-Brochure creation</li>
      <li>Inventory management</li>
      <li>Warehouse scanning</li>
      <li>Accounts &amp; ERP system</li>
    </ul>
    <span class="abs" style="left:14px;top:258px;font-size:11.5px;letter-spacing:.3px">integration</span>
    <span class="btn cta" style="left:97px;top:268px">Start Now</span>
  </article>
</section>

<section>
  <div class="abs access" role="img" aria-label="Soft blue background with a faint circuit-line pattern"></div>
  <h2 class="abs sec-title access-title">ACCESS OUR TECHNOLOGY</h2>

  <article class="abs panel green">
    <h3>PARTNER WITH US TO DEVELOP A CUSTOM APP</h3>
    <p>Whether you have an app in mind that needs developing or a business process requiring special attention our 20 plus years experience in start-ups, media and retailing means we’re the right people to help you bring it to life.</p>
    <span class="btn cta">Get Started</span>
  </article>
  <div class="abs halo" style="left:220px">
    <svg width="44" height="40" viewBox="0 0 44 40" fill="none" stroke="#0255a3" stroke-width="3" stroke-linejoin="round"><path d="M4 16l10-10 8 8-10 10z"/><path d="M22 6l8-4 10 10-10 10"/><path d="M12 24l8 8 10-10M16 20l8 8M20 16l8 8"/></svg>
  </div>

  <article class="abs panel yellow">
    <h3>INCORPORATE THE LATEST HARDWARE DEVICES AND TAGS TO BOOST BUSINESS</h3>
    <ul style="top:89px">
      <li>Glowbeacons – enhance customer’s in-store experience (Orchard)</li>
      <li>NFC tags – enhance customer’s in-store experience (Korvia)</li>
      <li>RFid tags- track global supply chains</li>
      <li>Video and movement sensors – for in-store retail insights</li>
    </ul>
    <span class="btn cta">Get Started</span>
  </article>
  <div class="abs halo" style="left:648px">
    <svg width="40" height="40" viewBox="0 0 40 40" fill="none" stroke="#0255a3" stroke-width="3"><rect x="10" y="3" width="26" height="26" rx="2"/><path d="M10 9h26" /><path d="M2 22h6v14H2zM8 24h10l6 4-6 4H8" fill="#0255a3"/></svg>
  </div>
</section>

<section>
  <h2 class="abs sec-title custom-title">CUSTOMISE OUR MOBILE AND WEB TECHNOLOGY<br>TO SUIT YOUR SUPPLY CHAIN</h2>

  <div class="abs feature wide" style="left:96px;top:1023px">
    <svg width="26" height="26" viewBox="0 0 26 26"><circle cx="13" cy="13" r="12" fill="#ec1f27"/><text x="13" y="19" text-anchor="middle" font-size="16" font-weight="700" fill="#fff" font-family="Open Sans,sans-serif">$</text></svg>
    <span style="margin-left:4px">COMMISSIONED SELLING</span>
  </div>
  <div class="abs feature" style="left:363px;top:1021px">
    <svg width="24" height="22" viewBox="0 0 24 22" fill="none" stroke="#ec1f27" stroke-width="2.5"><path d="M10 4H2v16h16v-6"/><path d="M8 14c2-6 6-8 12-8"/><path d="M16 2l5 4-5 4" fill="#ec1f27"/></svg>
    <span>EXPORT AND RETAIL MANAGEMENT</span>
  </div>
  <div class="abs feature wide" style="left:644px;top:1019px">
    <svg width="26" height="30" viewBox="0 0 26 30"><path d="M4 8l10-6 10 16-10 10-10-6z" fill="#ec1f27" transform="rotate(-20 13 15)"/><circle cx="10" cy="8" r="2" fill="#fff"/></svg>
    <span>MULTI-CHANNEL SELLING</span>
  </div>
  <div class="abs feature" style="left:149px;top:1055px">
    <svg width="24" height="24" viewBox="0 0 24 24" fill="#ec1f27"><circle cx="12" cy="8" r="4"/><path d="M5 22c0-6 3-9 7-9s7 3 7 9z"/><circle cx="3" cy="3" r="2.5"/><circle cx="21" cy="3" r="2.5"/><circle cx="3" cy="21" r="2.5"/><circle cx="21" cy="21" r="2.5"/></svg>
    <span>FLASH SALES CLEARANCE AND JOB LOTS</span>
  </div>
  <div class="abs feature wide" style="left:507px;top:1053px">
    <svg width="24" height="24" viewBox="0 0 24 24" fill="#ec1f27"><path d="M1 3h4l3 12h12l3-9H7" fill="none" stroke="#ec1f27" stroke-width="2.4"/><rect x="8" y="7" width="12" height="6"/><circle cx="9" cy="20" r="2.2"/><circle cx="19" cy="20" r="2.2"/></svg>
    <span>MANAGED OR DIY WEB &amp;BIDMART STORES</span>
  </div>
</section>

<footer>
  <div class="abs footer"></div>
  <div class="abs footer-mark">Lumen Peak</div>
  <div class="abs fcol" style="left:268px"><h4>ABOUT</h4><div>Who we are</div><div>Our Phylosophy</div><div>Company</div><div>News</div></div>
  <div class="abs fcol" style="left:405px"><h4>OUR PRODUCTS</h4><div>Custom Apps</div><div>Hardware Devices</div><div>Adipiscing elit</div><div>Nonummy</div></div>
  <div class="abs fcol" style="left:563px"><h4>LATEST NEWS</h4><div>Dolor sit amet</div><div>Consectetuer Adipiscing</div><div>Elit fur NYC</div><div>Ed diam nonummy Nbh</div></div>
  <div class="abs fcol" style="left:706px"><h4>CONTACT INFO</h4><div>+61 2 9040 7712</div><div>info@lumenpeak.com.au</div><div>12 Larkwood, 4C Marlowe,</div><div>Ashford City, USA</div></div>
  <div class="abs fbar">
    <span class="abs" style="left:96px">COPYRIGHT © LUMEN PEAK 2016</span>
    <span class="abs" style="left:590px">PRIVACY</span>
    <span class="abs" style="left:750px">TERMS &amp; POLICY</span>
  </div>
</footer>

</body>
</html>
```